Bramwick Vale Lamb - Online retail of "Meadow to Table" lamb

Design and publish our website that is google tracking friendly, SEO friendly and also allows a good shop using payloom payments.
Current website is www.bvgr.com.au. All the information and data is on there. for copy past.
Also include a recipe page. not a blog, but actual recipes we can change for seasons. i.e. hearty winter meals, v summer light and playful food.
We don't want anything complex, it needs to feel trustworthy, not to busy. make it easy to click and buy.

I also want to be able to update and manage myself once running, to reduce overheads.

Also ability to link post hive to the signup/contact information

Target Market(s)

people looking to save money and pay $15/kg, instead of supermarket chain $45/kg. People who like fresh, ethically grown produce.

Industry/Entity Type

Primary producer, Food

Coding

Coded - Design and coding required

Number of Pages Required

4 page

Font styles to use
Other font styles liked:
• Im not sure.

Requirements
Must have
• Easy functionality, trust worthy and easy use store/ordering, google tracking compatiable.
Nice to have
• Subscription, IE client signs up for a Half/Side of lamb delivered monthly for subscription fee

```html
<!DOCTYPE html>
<html lang="en">
<head>
<meta charset="UTF-8">
<title>Bramwick Vale Farms – Meadow to Table Lamb</title>
<link rel="stylesheet" href="https://fonts.googleapis.com/css2?family=Fredoka:wght@500;600&family=Quicksand:wght@500;600;700&display=swap">
<style>
:root{
  --black:#000;
  --ink:#0b0b0b;
  --footer:#232323;
  --field:#2a2a2a;
  --white:#fff;
  --muted:#e6e6e6;
  --grass-dark:#3d5a1e;
  --grass:#6f8f38;
  --wool:#d9d0bf;
  --line:#555;
}
*{box-sizing:border-box;margin:0;padding:0}
html,body{width:1200px;height:3339px;overflow:hidden;background:var(--black)}
body{position:relative;font-family:"Quicksand",sans-serif;color:var(--white)}
.abs{position:absolute}
.heading{font-family:"Fredoka",sans-serif;font-weight:600;letter-spacing:1px;text-transform:uppercase}

/* nav */
.site-nav{left:0;top:0;width:1200px;height:96px;background:var(--black);z-index:5}
.nav-link{top:44px;font-size:16px;font-weight:600;color:var(--white);text-decoration:none}
.brand-badge{left:513px;top:1px;width:174px;height:174px;border-radius:50%;background:var(--white);color:var(--black);display:flex;align-items:center;justify-content:center;text-align:center;font-weight:700;font-size:19px;line-height:1.2;z-index:6}
.search-btn{left:987px;top:30px;width:42px;height:42px;border-radius:50%;background:var(--white);z-index:6}

/* hero */
.hero{left:0;top:96px;width:1200px;height:591px;background:linear-gradient(100deg,var(--wool) 0%,#9aa86a 25%,var(--grass) 50%,var(--grass-dark) 100%)}
.hero-copy{left:724px;top:272px;width:440px}
.hero-kicker{font-size:26px}
.hero-title{font-size:37px;margin-top:12px}
.hero-text{font-size:25px;font-weight:600;line-height:40px;margin-top:20px}
.scallop{left:0;width:1200px;height:70px}

/* products */
.section-title{font-size:36px}
.product-photo{width:291px;height:311px;border-radius:40px}
.product-caption{width:291px;text-align:center;font-size:21px;line-height:29px;font-weight:500}
.price-btn{width:109px;height:54px;border:1.5px solid var(--white);border-radius:27px;display:flex;align-items:center;justify-content:center;font-size:21px;font-weight:700}
.slider-arrow{width:50px;height:50px;border-radius:50%;background:var(--white)}

/* signup */
.signup-title{left:110px;top:1505px;font-size:23px;line-height:48px}
.input-field{left:111px;width:486px;height:55px;background:var(--field);border-radius:4px;padding-left:29px;display:flex;align-items:center;font-size:15px;font-weight:600}
.outline-btn{border:1.5px solid var(--white);border-radius:28px;display:flex;align-items:center;justify-content:center;font-size:18px;font-weight:600;text-transform:uppercase}
.cloud-photo{left:728px;top:1475px;width:500px;height:427px;border-radius:48% 52% 45% 55%/55% 45% 55% 45%;border:10px solid #555;background:linear-gradient(180deg,#c7cfc2 0%,#8fae55 40%,#4d7a26 100%)}

/* about */
.about{left:0;top:1976px;width:1200px;height:492px;background:radial-gradient(ellipse at 75% 55%,#8c7a5c 0%,#4a5c2a 35%,#25360f 80%)}
.about-title{left:141px;top:2068px;font-size:36px}
.about-text{left:141px;top:2138px;width:440px;font-size:21px;font-weight:600;line-height:39px}

/* recipe */
.recipe{left:0;top:2468px;width:1200px;height:520px;background:var(--ink)}
.recipe-title{left:113px;top:2558px;font-size:36px}
.recipe-text{left:113px;top:2630px;width:430px;font-size:16px;font-weight:600;line-height:31.5px}
.recipe-photo{top:2574px;width:247px;height:251px;border-radius:14px}

/* footer */
.footer{left:0;top:2968px;width:1200px;height:371px;background:var(--footer)}
.col-title{top:3038px;font-size:22px;font-weight:600;text-transform:uppercase}
.col-list{top:3090px;list-style:none;font-size:16px;font-weight:600;line-height:33.6px}
.footer-brand{left:113px;top:3040px;width:160px;text-align:center;font-size:20px;font-weight:700;line-height:1.25}
.pay-name{left:113px;top:3180px;font-size:42px;font-weight:700}
.divider{left:111px;top:3284px;width:978px;height:1px;background:var(--line)}
.copyright{left:0;top:3300px;width:1200px;text-align:center;font-size:15px;font-weight:500}
.mail-partner{left:1128px;top:3212px;font-size:13px;font-weight:700;display:flex;align-items:center;gap:6px}
.mail-partner span{width:12px;height:12px;border-radius:50%;background:var(--white)}
</style>
</head>
<body>

<header class="abs site-nav">
  <a class="abs nav-link" style="left:184px" href="#">Home</a>
  <a class="abs nav-link" style="left:285px" href="#">About Us</a>
  <a class="abs nav-link" style="left:411px" href="#">Products</a>
  <a class="abs nav-link" style="left:732px" href="#">Recipe</a>
  <a class="abs nav-link" style="left:840px" href="#">Contact Us</a>
</header>
<div class="abs brand-badge">Bramwick<br>Vale Farms</div>
<div class="abs search-btn">
  <svg width="42" height="42" viewBox="0 0 42 42"><circle cx="19" cy="19" r="7" fill="none" stroke="#000" stroke-width="3"/><line x1="24" y1="24" x2="30" y2="30" stroke="#000" stroke-width="3.5" stroke-linecap="round"/></svg>
</div>

<section class="abs hero" role="img" aria-label="Photo of a woolly sheep standing in a green paddock"></section>
<div class="abs hero-copy">
  <p class="heading hero-kicker">Welcome to</p>
  <h1 class="heading hero-title">Bramwick Vale Farms!</h1>
  <p class="hero-text">Save money and pay $15/kg, instead of the supermarket chain $45/kg.</p>
</div>
<svg class="abs scallop" style="top:620px" viewBox="0 0 1200 70" preserveAspectRatio="none"><path d="M0 70V40a100 40 0 0 1 200 0a100 40 0 0 1 200 0a100 40 0 0 1 200 0a100 40 0 0 1 200 0a100 40 0 0 1 200 0a100 40 0 0 1 200 0V70Z" fill="#000"/></svg>

<h2 class="abs heading section-title" style="left:0;width:1200px;text-align:center;top:774px">Our Products</h2>

<div class="abs slider-arrow" style="left:36px;top:1125px"><svg width="50" height="50" viewBox="0 0 50 50"><path d="M36 25H14M22 17l-8 8 8 8" fill="none" stroke="#000" stroke-width="2.5" stroke-linecap="round" stroke-linejoin="round"/></svg></div>
<div class="abs slider-arrow" style="left:1114px;top:1125px"><svg width="50" height="50" viewBox="0 0 50 50"><path d="M14 25h22M28 17l8 8-8 8" fill="none" stroke="#000" stroke-width="2.5" stroke-linecap="round" stroke-linejoin="round"/></svg></div>

<div class="abs product-photo" style="left:117px;top:862px;background:linear-gradient(160deg,#7a4a33,#c98b86 50%,#5e3a2a)" role="img" aria-label="Packed prime lamb cuts laid out on a wooden table"></div>
<p class="abs product-caption" style="left:117px;top:1193px">Fresh Whole Lamb - Prime Cut Pack - $16.50 per kilogram</p>
<div class="abs price-btn" style="left:209px;top:1308px">$100</div>

<div class="abs product-photo" style="left:452px;top:914px;background:linear-gradient(180deg,#2a1a10,#6b3a1a 45%,#f0a020 75%,#3a1a0a)" role="img" aria-label="Whole lamb roasting on a spit over an open fire"></div>
<p class="abs product-caption" style="left:452px;top:1245px">Fresh Lamb spit roast - Approx final cost $250 Feeds 20 people!</p>
<div class="abs price-btn" style="left:545px;top:1360px">$150</div>

<div class="abs product-photo" style="left:788px;top:862px;background:linear-gradient(150deg,#e9e6df,#7b4d2a 45%,#5a7a2a 80%,#c94a2a)" role="img" aria-label="Plate of lamb mince meatballs with tomatoes and yoghurt dip"></div>
<p class="abs product-caption" style="left:788px;top:1193px">Lamb Mince - $10 per kg Minimum order 5kgs for free delivery</p>
<div class="abs price-btn" style="left:880px;top:1308px">$50</div>

<h2 class="abs heading signup-title">Sign up for a half/side of lamb delivered monthly<br>for subscription fee</h2>
<div class="abs input-field" style="top:1633px">Full Name</div>
<div class="abs input-field" style="top:1705px">Email Address</div>
<div class="abs outline-btn" style="left:111px;top:1792px;width:152px;height:54px">Subscribe</div>
<div class="abs cloud-photo" role="img" aria-label="Sheep standing in a green field"></div>

<section class="abs about" role="img" aria-label="Flock of sheep in a paddock with one sheep in front"></section>
<h2 class="abs heading about-title">About Us</h2>
<p class="abs about-text">At Bramwick Vale Farms, we're more than just a farm; we're a sanctuary dedicated to bringing you the finest, juiciest lamb products while having a blast doing it!</p>
<div class="abs outline-btn" style="left:141px;top:2316px;width:169px;height:54px">Learn More</div>

<section class="abs recipe"></section>
<h2 class="abs heading recipe-title">Recipe</h2>
<p class="abs recipe-text">Sed ut perspiciatis unde omnis iste natus error sit voluptatem accusantium doloremque laudantium, totam rem aperiam, eaque ipsa quae ab illo inventore veritatis et quasi architecto beatae vitae dicta sunt</p>
<div class="abs outline-btn" style="left:113px;top:2787px;width:168px;height:55px">View Recipes</div>
<div class="abs recipe-photo" style="left:588px;background:linear-gradient(150deg,#2a1a10,#6b3a20 50%,#3a4a1a)" role="img" aria-label="Roasted lamb cutlets with herbs"></div>
<div class="abs recipe-photo" style="left:842px;background:radial-gradient(circle at 55% 50%,#8a3a30 0%,#b36a55 25%,#fff 55%)" role="img" aria-label="Seared lamb steaks on a white plate"></div>
<svg class="abs" style="left:1098px;top:2684px" width="40" height="30" viewBox="0 0 40 30"><path d="M20 5a10 10 0 1 0 0 20" fill="none" stroke="#fff" stroke-width="2"/><path d="M12 15h24M30 9l6 6-6 6" fill="none" stroke="#fff" stroke-width="2" stroke-linecap="round" stroke-linejoin="round"/></svg>

<footer class="abs footer"></footer>
<svg class="abs scallop" style="top:2900px" viewBox="0 0 1200 70" preserveAspectRatio="none"><path d="M0 70V40a115 40 0 0 1 230 0a115 40 0 0 1 230 0a115 40 0 0 1 230 0a115 40 0 0 1 230 0a115 40 0 0 1 230 0a115 40 0 0 1 230 0V70Z" fill="#232323"/></svg>
<div class="abs footer-brand">Bramwick Vale Farms</div>
<div class="abs pay-name">payloom</div>

<h3 class="abs col-title" style="left:352px">Quick Links</h3>
<ul class="abs col-list" style="left:352px"><li>Home</li><li>About Us</li><li>Products</li><li>Recipe</li><li>Contact Us</li></ul>
<h3 class="abs col-title" style="left:581px">Social Media</h3>
<ul class="abs col-list" style="left:581px"><li>Friendbook</li><li>Snapgram</li><li>Chirper</li></ul>
<h3 class="abs col-title" style="left:814px">Contact Details</h3>
<ul class="abs col-list" style="left:814px"><li>0400 218 647</li><li>hello@bvgr.com.au</li><li>14 Fernhollow Road, Bramwick Vale</li><li>3960</li></ul>
<div class="abs mail-partner"><span></span>post hive</div>

<div class="abs divider"></div>
<p class="abs copyright">@2023 COPYRIGHTS. ALL RIGHTS RESERVED.</p>

</body>
</html>
```